CD face & Jewel Case Design for Bayou Lanternmen Band

We need CD packaging (jewel case with 2 panel insert, and CD disc face) designed for the band Bayou Lanternmen.

Hear a sample of the music at: https://clipvault.example/watch/k7Rm2xQ9

It should say "Bayou Lanternmen" prominently on the cover and disc face since that's the album name too. The final design should communicate fun, energy and appeal to all ages.

There are many photos to choose from and we encourage you to be creative and follow your muse.

The text for album credits/liner notes is in the file "TEXT CREDITS".

We are open to your ideas. The templates have been uploaded as .psd files - if you need in another format, please specify thanks :)

Target Market(s)

fans of zydeco music, rock, counrty, all ages

Requirements
Nice to have
• maybe a retro look but not mandatory

```html
<!DOCTYPE html>
<html lang="en">
<head>
<meta charset="utf-8">
<title>Bayou Lanternmen – CD Insert and Disc Face</title>
<link rel="stylesheet" href="https://fonts.googleapis.com/css2?family=Didact+Gothic&display=swap">
<style>
  :root {
    --page: #f1f1f1;
    --paper: #ffffff;
    --ink: #3a3a3a;
    --ink-soft: #6a6a6a;
    --brand: #5b3d8c;
    --pink: #e8459b;
    --blue: #3aa6dc;
    --green: #8cc63f;
    --orange: #f5a623;
    --hub: #d6d6d6;
    --hub-ring: #a9a9a9;
    --hub-inner: #c4c4c4;
    --rim: #cfcfcf;
  }
  * { margin: 0; padding: 0; box-sizing: border-box; }
  html, body { width: 1200px; height: 800px; overflow: hidden; }
  body {
    background: var(--page);
    font-family: "Didact Gothic", sans-serif;
    color: var(--ink);
    position: relative;
  }

  /* Insert panel */
  .insert {
    position: absolute;
    left: 70px; top: 140px;
    width: 500px; height: 500px;
    background: var(--paper);
    box-shadow: 0 2px 10px rgba(0,0,0,.12);
    overflow: hidden;
  }
  .insert__art {
    position: absolute; inset: 0;
    background:
      radial-gradient(circle at 8% 28%, rgba(232,69,155,.55), transparent 14%),
      radial-gradient(circle at 12% 42%, rgba(140,198,63,.5), transparent 12%),
      radial-gradient(circle at 38% 4%, rgba(245,166,35,.55), transparent 16%),
      radial-gradient(circle at 70% 2%, rgba(58,166,220,.55), transparent 22%),
      radial-gradient(circle at 96% 30%, rgba(232,69,155,.35), transparent 18%),
      radial-gradient(circle at 92% 70%, rgba(58,166,220,.45), transparent 18%),
      radial-gradient(circle at 60% 55%, rgba(140,198,63,.25), transparent 25%),
      radial-gradient(circle at 30% 60%, rgba(58,166,220,.25), transparent 25%);
  }
  .insert__photo {
    position: absolute; left: 0; right: 0; bottom: 0;
    height: 175px;
    background: linear-gradient(180deg, rgba(255,255,255,0) 0%, rgba(190,190,195,.75) 35%, rgba(150,150,160,.85) 60%, rgba(232,69,155,.35) 100%);
  }
  .logo {
    position: absolute; left: 0; right: 0; top: 22px;
    display: flex; align-items: center; justify-content: center; gap: 8px;
  }
  .logo__dot { width: 14px; height: 14px; border-radius: 50%; background: var(--brand); }
  .logo__name { font-size: 26px; color: var(--brand); letter-spacing: .5px; }

  .tracklist {
    position: absolute; top: 68px;
    font-size: 11px; line-height: 1.35;
    list-style: none;
  }
  .tracklist__side { font-size: 10px; letter-spacing: 1px; margin-bottom: 2px; }
  .tracklist--one { left: 66px; }
  .tracklist--two { left: 290px; }
  .tracklist li span { display: inline-block; width: 16px; }

  .credits {
    position: absolute; left: 90px; right: 90px; top: 210px;
    text-align: center;
    font-size: 7.5px; line-height: 1.45; color: var(--ink-soft);
  }
  .credits p { margin-bottom: 7px; }

  /* Disc */
  .disc { position: absolute; left: 610px; top: 130px; }
  .disc__name { font-family: "Didact Gothic", sans-serif; font-size: 22px; fill: var(--brand); }
  .disc__side { font-family: "Didact Gothic", sans-serif; font-size: 15px; fill: var(--pink); }
  .disc__dot { fill: var(--brand); }
  .disc__rim { fill: none; stroke: var(--rim); stroke-width: 2; }
  .disc__hub { fill: var(--hub); }
  .disc__ring { fill: none; stroke: var(--hub-ring); stroke-width: 3; }
  .disc__inner { fill: var(--hub-inner); }
  .disc__hole { fill: var(--page); }
</style>
</head>
<body>

<section class="insert" aria-label="Inside insert panel">
  <div class="insert__art" role="img" aria-label="Colourful swirl and halftone dot artwork"></div>
  <div class="insert__photo" role="img" aria-label="Band photograph, five musicians with instruments"></div>

  <div class="logo">
    <span class="logo__dot"></span>
    <span class="logo__name">Bayou Lanternmen</span>
  </div>

  <ol class="tracklist tracklist--one">
    <li class="tracklist__side">SIDE ONE</li>
    <li><span>1</span>Lantern On The Levee</li>
    <li><span>2</span>Let's Go Wandering</li>
    <li><span>3</span>Bayou Runaway</li>
    <li><span>4</span>Can't Sit Still Tonight</li>
    <li><span>5</span>Moonlight On The Marsh</li>
    <li><span>6</span>Two-Step Round The Globe</li>
    <li><span>7</span>Midnight Parlour</li>
  </ol>

  <ol class="tracklist tracklist--two">
    <li class="tracklist__side">SIDE TWO</li>
    <li><span>8</span>Worn And Weary</li>
    <li><span>9</span>Sweetest Kinda Sleep</li>
    <li><span>10</span>Lady Of The Pier</li>
    <li><span>11</span>Ten Thousand Miles Of Squeezebox</li>
    <li><span>12</span>Cypress Trees By The River</li>
  </ol>

  <div class="credits">
    <p>“Can't Sit Still Tonight” &amp; “Worn And Weary” written &amp; arr. by Rhett Calloway (CRG), © 2015 Marigold Lane Music (CRG).<br>
    All other songs written by Dom Arceneaux, © 2015 Marigold Lane Music (CRG).<br>
    This recording ℗ 2015, 2016 by Bayou Lanternmen.</p>
    <p>Jules Broussard: keyboard<br>
    Lionel Hebert: electric guitar, backing vocals<br>
    Dom Arceneaux: Cajun accordion, vocals<br>
    Luc Thibodeaux: drums, backing vocals<br>
    Rhett Calloway: bass guitar, vocals</p>
    <p>Produced by Bayou Lanternmen<br>
    Recorded &amp; mixed by Sam Delacroix at Harbor Room Studios, Dockside, NY<br>
    Additional recording by Glen Fontenot at Copperline Sound, Millbrook, NJ<br>
    Mastered in Lakeport by Theo Calloway</p>
    <p>Snow photography by Ivy Laurent<br>
    Night photography by Noel Prejean</p>
    <p>bayoulanternmen.example<br>
    Social: /bayoulanternmen<br>
    Updates: @bayoulanternmen<br>
    Photos: bayoulanternmen<br>
    hello@bayoulanternmen.example</p>
  </div>
</section>

<svg class="disc" width="520" height="520" viewBox="0 0 520 520" aria-label="CD disc face">
  <defs>
    <clipPath id="disc-shape"><circle cx="260" cy="260" r="255"/></clipPath>
    <linearGradient id="disc-art-tone" x1="0" y1="0" x2="1" y2="1">
      <stop offset="0" stop-color="#7fc3e8"/>
      <stop offset=".35" stop-color="#c9e59b"/>
      <stop offset=".6" stop-color="#f3a9cf"/>
      <stop offset="1" stop-color="#8fcbee"/>
    </linearGradient>
    <linearGradient id="disc-photo-tone" x1="0" y1="0" x2="0" y2="1">
      <stop offset="0" stop-color="#d8d8dc" stop-opacity="0"/>
      <stop offset=".3" stop-color="#b8b8c0"/>
      <stop offset="1" stop-color="#8e8e98"/>
    </linearGradient>
  </defs>
  <g clip-path="url(#disc-shape)">
    <rect class="disc__art" width="520" height="520" fill="url(#disc-art-tone)" role="img" aria-label="Colourful swirl and halftone dot artwork"/>
    <rect class="disc__photo" x="0" y="330" width="520" height="190" fill="url(#disc-photo-tone)" role="img" aria-label="Band photograph, five musicians with instruments"/>
  </g>
  <circle class="disc__rim" cx="260" cy="260" r="255"/>

  <circle class="disc__dot" cx="150" cy="85" r="6"/>
  <text class="disc__name" x="163" y="93">Bayou Lanternmen</text>
  <text class="disc__side" x="232" y="122">side one</text>

  <circle class="disc__hub" cx="260" cy="260" r="78"/>
  <circle class="disc__ring" cx="260" cy="260" r="58"/>
  <circle class="disc__inner" cx="260" cy="260" r="40"/>
  <circle class="disc__hole" cx="260" cy="260" r="18"/>
</svg>

</body>
</html>
```